Flyer for Clothing Line Launch Event

I need a flyer designed for the launch of my women's clothing line in February 2016. I will need to use this flyer on my website, social media and print.

The Collections

Our contemporary collections are comprised of influences drawing from bohemian and chic motifs. The term "Bohemian" is described as "simply an artist or littérateur who, consciously or unconsciously, secedes from conventionality in life and in art". "Chic" was borrowed from the French in the late 19th century and has come to mean stylish or elegant.

About my company:

We design free and romantic garments targeted to fashion-forward women driven by uniqueness and desire to accentuate her confidence and class through style. We look forward to our clients indulging in the LorettaVance brand to include our Keystone Circle, Lend-A-Heart, eNewsletters, Trunk Shows and Fashion Shows.

Target Market(s)

upscale women ages 30-50

Industry/Entity Type

Fashion

Font styles to use
Decorative
Script
Other font styles liked:
• Handwritten type script

Colors
000000
f37122
3377b5
e667a6

Requirements
Must have
• colors similar to my website boutique.lorettavance-example.com
• my logo
Nice to have
• image from my website
• my logo

```html
<!DOCTYPE html>
<html lang="en">
<head>
<meta charset="utf-8">
<title>LorettaVance Boutique Launch Flyer</title>
<link href="https://fonts.googleapis.com/css2?family=Josefin+Sans:wght@300;400&family=Lora:ital@1&display=swap" rel="stylesheet">
<style>
  :root {
    --burgundy: #8e2a1f;
    --orange: #e8762a;
    --orange-deep: #c95e18;
    --ink-white: #ffffff;
    --panel-white: rgba(255, 255, 255, 0.82);
    --photo-top: #6f6656;
    --photo-mid: #b9b3a8;
    --photo-low: #d8d4cc;
    --photo-ground: #a9a49b;
    --street-left: #5b5346;
    --street-right: #8d8a84;
    --dress-light: #ecebe7;
    --dress-shade: #cfcbc4;
  }
  * { margin: 0; padding: 0; box-sizing: border-box; }
  html, body { width: 874px; height: 1200px; overflow: hidden; }
  body { background: #ffffff; font-family: "Josefin Sans", sans-serif; }

  .flyer { position: relative; width: 874px; height: 1200px; overflow: hidden; }

  .hero-photo { position: absolute; inset: 0; overflow: hidden; }
  .hero-photo .street {
    position: absolute; inset: 0;
    background:
      linear-gradient(90deg, var(--street-left) 0%, rgba(91,83,70,0) 30%, rgba(141,138,132,0) 70%, var(--street-right) 100%),
      linear-gradient(180deg, var(--photo-top) 0%, #948b7a 20%, var(--photo-mid) 45%, var(--photo-low) 65%, var(--photo-ground) 100%);
    opacity: 0.95;
  }
  .hero-photo .subject {
    position: absolute; left: 250px; top: 40px; width: 300px; height: 1110px;
    border-radius: 140px 140px 60px 60px;
    background: linear-gradient(180deg, #4a3a30 0%, #6b5243 14%, var(--dress-light) 24%, var(--dress-shade) 55%, var(--dress-light) 78%, #d9c59a 92%, #c9b07c 100%);
    opacity: 0.75;
  }

  .monogram-mark {
    position: absolute; left: 372px; top: 420px; width: 130px; height: 130px;
    border: 2px solid var(--burgundy); border-radius: 50%;
  }

  .brand-wordmark {
    position: absolute; left: 0; right: 0; top: 588px;
    text-align: center;
    font-weight: 300; font-size: 84px; letter-spacing: 3px; line-height: 1;
    color: var(--burgundy);
    text-transform: uppercase; white-space: nowrap;
  }

  .event-card { position: absolute; left: 486px; top: 690px; width: 388px; }

  .intro-band {
    background: var(--orange);
    height: 90px; padding: 18px 0 0 26px; color: var(--ink-white);
  }
  .intro-band .eyebrow { font-size: 13px; letter-spacing: 1.5px; text-transform: uppercase; }
  .intro-band .title { font-size: 29px; margin-top: 10px; white-space: nowrap; }

  .date-band {
    position: relative; width: 282px; height: 55px; margin-top: 10px;
    background: var(--burgundy); color: var(--ink-white);
    font-size: 30px; padding: 13px 0 0 26px; white-space: nowrap;
  }
  .date-band svg { position: absolute; right: -22px; top: 0; }

  .invite-panel {
    background: var(--panel-white); height: 265px; padding: 22px 26px 0;
    color: var(--burgundy); font-family: "Lora", serif; font-style: italic;
  }
  .invite-panel .lead { font-size: 19px; line-height: 1.3; }
  .invite-panel .details { font-size: 15px; line-height: 1.5; margin-top: 22px; color: var(--orange-deep); }
  .invite-panel .web {
    font-family: "Josefin Sans", sans-serif; font-style: normal;
    font-size: 15px; letter-spacing: 1px; margin-top: 26px; color: var(--burgundy);
  }
</style>
</head>
<body>
<main class="flyer">
  <div class="hero-photo" role="img" aria-label="Photograph of the designer standing on a city pedestrian street in a white off-shoulder dress and gold heels">
    <div class="street"></div>
    <div class="subject"></div>
  </div>

  <div class="monogram-mark" aria-hidden="true"></div>
  <h1 class="brand-wordmark">LorettaVance</h1>

  <section class="event-card">
    <div class="intro-band">
      <p class="eyebrow">Introducing</p>
      <p class="title">LorettaVance Boutique</p>
    </div>
    <div class="date-band">
      February 20, 2016
      <svg width="22" height="55" viewBox="0 0 22 55"><polygon points="0,0 22,27.5 0,55" fill="#8e2a1f"/></svg>
    </div>
    <div class="invite-panel">
      <p class="lead">Please join<br>designer LorettaVance<br>for her Collection Launch Series</p>
      <p class="details">Saturday Noon to Six<br>Riverside Showroom</p>
      <p class="web">www.lorettavance-example.com</p>
    </div>
  </section>
</main>
</body>
</html>
```